Bluestone Advisory & Mgmt - Professional Business Cards

Hi!

I am a Real Estate Developer and Construction Consultant.

I have a lot of inspiration from previous designs and would be open to using the attached Designs as a starting point. I would like to see these styles incorporated into your designs.

I really need professional business card to go with it that includes my important info.

Look forward to seeing your designs!.

Target Market(s)

My Target market are building owners, lawyers, consultants.

Industry/Entity Type

Real Estate Development

Contact Information for Business Card

My Name: Dorian Pelkey
My Title: Principle
Company Name: Bluestone Advisory & Mgmt, LLC
Address: 348 West 71st Street, 9th FL New York, NY 10010
Mobile: 917.806.3971
Website: bam-hvx.example

Font styles to use
Serif
Sans Serif

Colors

Designer to choose colors to be used in the design.

Requirements
Must have
• Must incorporate the logo attached or have new that looks similar.
• Must use professional font that will be seen and judged by wealthy land owners and developers.
• Must incorporate some of the color green.
Should not have
• Photo's or pictures of people or buildings of any kind.

```html
<!DOCTYPE html>
<html lang="en">
<head>
<meta charset="utf-8">
<title>Bluestone Advisory &amp; Mgmt – Business Cards</title>
<link href="https://fonts.googleapis.com/css2?family=Lato:wght@400;700&display=swap" rel="stylesheet">
<style>
  :root {
    --brand-green: #4fb577;
    --text-grey: #8a8585;
    --card-white: #ffffff;
    --backdrop: #e9e7e4;
  }
  * { margin: 0; padding: 0; box-sizing: border-box; }
  html, body { width: 1000px; height: 1200px; overflow: hidden; }
  body {
    background: var(--backdrop);
    font-family: "Lato", Arial, sans-serif;
    position: relative;
  }
  .card {
    position: absolute;
    box-shadow: 0 6px 14px rgba(0,0,0,0.18);
  }
  .card-front {
    left: 110px; top: 120px; width: 778px; height: 446px;
    background: var(--card-white);
  }
  .card-back {
    left: 109px; top: 633px; width: 781px; height: 447px;
    background: var(--brand-green);
  }
  .wordmark {
    position: absolute;
    font-weight: 700;
    line-height: 1.05;
  }
  .wordmark-name { display: block; font-size: 56px; letter-spacing: -1px; }
  .wordmark-sub { display: block; font-size: 21px; margin-top: 6px; }
  .card-front .wordmark {
    left: 76px; top: 150px; color: var(--brand-green);
  }
  .card-back .wordmark {
    left: 0; right: 0; top: 150px; text-align: center; color: var(--card-white);
  }
  .card-back .wordmark-name { font-size: 70px; }
  .card-back .wordmark-sub { font-size: 26px; }
  .divider {
    position: absolute; left: 364px; top: 112px;
    width: 3px; height: 220px; background: var(--brand-green);
  }
  .contact {
    position: absolute; left: 405px; top: 104px;
    color: var(--text-grey);
  }
  .person-name {
    font-size: 26px; font-weight: 700; color: var(--brand-green);
  }
  .person-title { font-size: 19px; margin-top: 4px; }
  .company-name {
    font-size: 18px; font-weight: 700; color: var(--brand-green);
    margin-top: 15px;
  }
  .contact-list { list-style: none; margin-top: 14px; }
  .contact-item {
    display: flex; align-items: flex-start; gap: 9px;
    font-size: 18px; line-height: 31px;
  }
  .contact-item svg { flex: none; margin-top: 7px; }
  .contact-item .icon-spacer { width: 18px; flex: none; }
  .back-url {
    position: absolute; left: 0; right: 0; top: 385px;
    text-align: center; color: var(--card-white); font-size: 20px;
  }
</style>
</head>
<body>
  <section class="card card-front">
    <div class="wordmark">
      <span class="wordmark-name">Bluestone</span>
      <span class="wordmark-sub">Advisory &amp; Management</span>
    </div>
    <div class="divider"></div>
    <div class="contact">
      <h1 class="person-name">Dorian Pelkey</h1>
      <p class="person-title">Principle</p>
      <p class="company-name">Bluestone Advisory &amp; Mgmt, LLC</p>
      <ul class="contact-list">
        <li class="contact-item">
          <svg width="18" height="18" viewBox="0 0 24 24" fill="none" stroke="var(--brand-green)" stroke-width="2.4"><path d="M12 22s-7-7-7-12a7 7 0 0 1 14 0c0 5-7 12-7 12z"/><circle cx="12" cy="10" r="2.6"/></svg>
          <span>348 West 71st Street</span>
        </li>
        <li class="contact-item"><span class="icon-spacer"></span><span>9th FL New York, NY 10010</span></li>
        <li class="contact-item">
          <svg width="18" height="18" viewBox="0 0 24 24" fill="var(--brand-green)"><path d="M6.6 10.8a15.2 15.2 0 0 0 6.6 6.6l2.2-2.2a1 1 0 0 1 1-.25 11.4 11.4 0 0 0 3.6.57 1 1 0 0 1 1 1V20a1 1 0 0 1-1 1A17 17 0 0 1 3 4a1 1 0 0 1 1-1h3.5a1 1 0 0 1 1 1c0 1.25.2 2.45.57 3.57a1 1 0 0 1-.25 1z"/></svg>
          <span>917.806.3971</span>
        </li>
        <li class="contact-item">
          <svg width="18" height="18" viewBox="0 0 24 24" fill="none" stroke="var(--brand-green)" stroke-width="2"><circle cx="12" cy="12" r="9"/><path d="M3 12h18M12 3c3 3.2 3 14.8 0 18M12 3c-3 3.2-3 14.8 0 18"/></svg>
          <span>bam-hvx.example</span>
        </li>
      </ul>
    </div>
  </section>

  <section class="card card-back">
    <div class="wordmark">
      <span class="wordmark-name">Bluestone</span>
      <span class="wordmark-sub">Advisory &amp; Management</span>
    </div>
    <p class="back-url">bam-hvx.example</p>
  </section>
</body>
</html>
```